Law Firm Brochure www.brantwicklaw.com

Our law firm is expanding into Allegany, Frederick, and Washington County, very few attorneys, however it's a very small town and generally the residents don't trust out of town attorneys. Our firm is has two partners. Margaret Dunleavy and Peter Wrobly. Margaret is from Allegany County. MargAret also sits on the Board of Governors for the TCLG representing theses counties. The firm has opened a new office in Cumberland. The firm wants to attract business owners and banks to focus more on the representing their interests. Because the firm has a Rockville officethe firm can easily compete and out price virtually all the Metropolitan large firms in litigation, bankruptcy, domestic, contract or reorganization. Because the firm appears young, both partners are older than the appear, they have had difficulty getting foothold in these counties, however both have been practicing and are well respected members and are past and present officers of many specialty bar association and boards. They have combined 40 years legal experience.

Target Market(s)

business owners, banks in western Maryland.

Industry/Entity Type

Attorney

Font styles to use
Sans Serif

Requirements
Must have
• Ask Titans, Sharper or Larger? Keen Counsel Take Verdicts.
• Attorney Profiles, Practice Areas, Contact Information, Awards, Appointments, Bar Memberships, and Board Positions
• www.brantwicklaw.com
Nice to have
• Use color themes from our logo

```html
<!DOCTYPE html>
<html lang="en">
<head>
<meta charset="utf-8">
<title>Brantwick Law Trifold Brochure</title>
<link rel="stylesheet" href="https://fonts.googleapis.com/css2?family=Lato:ital,wght@0,400;0,700;0,900;1,700;1,900&display=swap">
<style>
  :root {
    --navy: #1d3f79;
    --navy-deep: #173466;
    --orange: #f47c20;
    --white: #ffffff;
    --ink: #2b2b2b;
    --stage: #e6e6e4;
    --photo-warm: #cdbfb4;
    --photo-light: #f1eeeb;
  }
  * { box-sizing: border-box; margin: 0; padding: 0; }
  html, body { width: 1200px; height: 1040px; overflow: hidden; }
  body {
    background: var(--stage);
    font-family: "Lato", Arial, sans-serif;
    color: var(--ink);
  }
  .brochure {
    position: absolute;
    left: 15px; top: 65px;
    width: 1170px; height: 910px;
    display: flex;
    box-shadow: 0 6px 24px rgba(0,0,0,.18);
  }
  .panel { position: relative; width: 390px; height: 100%; overflow: hidden; }

  .site-band {
    position: absolute; left: 0; right: 0; bottom: 0; height: 62px;
    display: flex; align-items: center; justify-content: center;
    font-weight: 700; font-size: 17px; letter-spacing: 5px;
  }
  .wordmark {
    font-weight: 400; text-transform: uppercase; line-height: 1.02;
    display: flex; align-items: center; gap: 12px;
  }
  .wordmark .mark { width: 14px; height: 14px; background: var(--orange); flex: none; }

  /* inside panel */
  .panel-inside { background: var(--white); padding: 34px 26px 0 26px; }
  .pill { display: flex; align-items: center; height: 46px; margin-bottom: 14px; }
  .pill .disc {
    width: 50px; height: 50px; border-radius: 50%;
    background: var(--white); border: 5px solid var(--navy); flex: none;
    position: relative; z-index: 1;
    box-shadow: inset 0 0 0 3px var(--orange);
  }
  .pill .label {
    background: var(--navy); color: var(--white);
    font-weight: 900; font-style: italic; font-size: 24px;
    height: 34px; line-height: 34px; padding: 0 22px 0 20px; margin-left: -12px;
    border-radius: 0 18px 18px 0;
  }
  .pill .label span { color: var(--orange); }
  .practice-list {
    list-style: none; display: grid; grid-template-columns: 1fr 1fr;
    row-gap: 8px; margin: 4px 0 22px 2px; font-size: 17px;
  }
  .practice-list li { display: flex; align-items: center; gap: 8px; }
  .practice-list svg { width: 14px; height: 14px; flex: none; }
  .about-text p { font-size: 14px; line-height: 1.36; text-align: justify; margin-bottom: 10px; }
  .about-text strong { color: var(--navy); font-weight: 700; }
  .panel-inside .wordmark {
    color: var(--navy); font-size: 21px; justify-content: center; margin: 12px 0 0;
  }
  .team-photo {
    position: absolute; left: 0; right: 0; bottom: 62px; height: 170px;
    background: linear-gradient(180deg, #d9d6d3 0%, #5a5a60 55%, #f4f4f4 100%);
  }
  .call-box {
    position: absolute; left: 30px; right: 30px; bottom: 108px; height: 66px;
    background: var(--white); text-align: center; padding-top: 8px;
    box-shadow: 0 1px 4px rgba(0,0,0,.2);
  }
  .call-box .lead { color: var(--navy); font-weight: 700; font-size: 16px; }
  .call-box .phone { color: var(--orange); font-weight: 700; font-size: 27px; line-height: 1.1; }
  .panel-inside .site-band { background: var(--orange); color: var(--white); }

  /* contact panel */
  .panel-contact { background: var(--navy); color: var(--white); text-align: center; }
  .tower {
    position: absolute; left: 40px; right: 40px; top: 60px; height: 780px;
    background: linear-gradient(160deg, rgba(255,255,255,.09), rgba(255,255,255,0) 70%);
  }
  .contact-body { position: relative; padding-top: 260px; }
  .panel-contact .wordmark { color: var(--white); font-size: 26px; justify-content: center; }
  .headline { color: var(--orange); font-weight: 700; font-size: 21px; line-height: 1.3; margin: 34px 30px 10px; }
  .subline { color: var(--orange); font-weight: 700; font-size: 15.5px; line-height: 1.4; margin: 0 40px 42px; }
  .contacts { list-style: none; font-size: 13px; line-height: 1.35; }
  .contacts li { margin-bottom: 8px; display: flex; justify-content: center; gap: 7px; }
  .contacts svg { width: 12px; height: 12px; flex: none; margin-top: 2px; }
  .contacts .big { font-size: 20px; }
  .contacts .big svg { width: 16px; height: 16px; margin-top: 5px; }
  .panel-contact .site-band { background: var(--white); color: var(--orange); }

  /* cover panel */
  .panel-cover { background: var(--navy); }
  .cover-top {
    position: absolute; left: 0; right: 0; top: 0; height: 190px;
    background: var(--white); border-top: 10px solid var(--navy); border-bottom: 8px solid var(--orange);
    display: flex; align-items: center; justify-content: center;
  }
  .cover-top .wordmark { color: var(--navy); font-size: 32px; }
  .partners-photo {
    position: absolute; left: 0; right: 0; top: 190px; height: 510px;
    background: radial-gradient(ellipse at 50% 45%, var(--photo-light) 0%, var(--photo-warm) 55%, #3a3336 100%);
    border-bottom: 6px solid var(--white);
  }
  .tagline { position: absolute; left: 20px; right: 20px; top: 728px; text-align: center; }
  .tagline .ask { color: var(--orange); font-weight: 900; font-style: italic; font-size: 29px; line-height: 1.12; text-transform: uppercase; }
  .tagline .claim { color: var(--white); font-size: 25px; margin-top: 10px; }
  .panel-cover .site-band { background: var(--orange); color: var(--white); }
</style>
</head>
<body>
<main class="brochure">

  <section class="panel panel-inside">
    <div class="pill"><div class="disc"></div><div class="label">We <span>offer</span></div></div>
    <ul class="practice-list">
      <li><svg viewBox="0 0 14 14"><path d="M1 8l4 4 8-10" stroke="#f47c20" stroke-width="2.6" fill="none"/></svg>Bankruptcy</li>
      <li><svg viewBox="0 0 14 14"><path d="M1 8l4 4 8-10" stroke="#f47c20" stroke-width="2.6" fill="none"/></svg>Domestic</li>
      <li><svg viewBox="0 0 14 14"><path d="M1 8l4 4 8-10" stroke="#f47c20" stroke-width="2.6" fill="none"/></svg>Criminal Defense</li>
      <li><svg viewBox="0 0 14 14"><path d="M1 8l4 4 8-10" stroke="#f47c20" stroke-width="2.6" fill="none"/></svg>MVA</li>
      <li><svg viewBox="0 0 14 14"><path d="M1 8l4 4 8-10" stroke="#f47c20" stroke-width="2.6" fill="none"/></svg>DUI/DWI</li>
      <li><svg viewBox="0 0 14 14"><path d="M1 8l4 4 8-10" stroke="#f47c20" stroke-width="2.6" fill="none"/></svg>Traffic</li>
      <li><svg viewBox="0 0 14 14"><path d="M1 8l4 4 8-10" stroke="#f47c20" stroke-width="2.6" fill="none"/></svg>Contracts</li>
      <li><svg viewBox="0 0 14 14"><path d="M1 8l4 4 8-10" stroke="#f47c20" stroke-width="2.6" fill="none"/></svg>Civil Litigation</li>
    </ul>
    <div class="pill"><div class="disc"></div><div class="label">About <span>us</span></div></div>
    <div class="about-text">
      <p>As an award winning law firm, our attorneys are known for being hard working, creative, and results driven. Partners <strong>Margaret Dunleavy</strong> and <strong>Peter Wrobly</strong> bring over 40 years combined experience to business owners and banks in litigation, bankruptcy and reorganization.</p>
      <p>Margaret, raised in Allegany County, sits on the TCLG Board of Governors for the western counties. Both partners are admitted Maryland bar members, hold court appointments, and are past and present officers of specialty bar associations and boards, here to help you through the most difficult times.</p>
    </div>
    <div class="wordmark"><span class="mark"></span><span>Brantwick<br>Law LLC</span></div>
    <div class="team-photo" role="img" aria-label="Photo of a large group of business professionals standing in a row"></div>
    <div class="call-box">
      <div class="lead">For more information, call us today</div>
      <div class="phone">301.555.0148</div>
    </div>
    <div class="site-band">www.brantwicklaw.com</div>
  </section>

  <section class="panel panel-contact">
    <div class="tower" role="img" aria-label="Faint photo of a glass office tower"></div>
    <div class="contact-body">
      <div class="wordmark"><span class="mark"></span><span>Brantwick<br>Law LLC</span></div>
      <p class="headline">We offer dynamic, creative, and inspired representation.</p>
      <p class="subline">We are veteran trial attorneys with over 40 years combined experience in Federal and State Courts.</p>
      <ul class="contacts">
        <li class="big"><svg viewBox="0 0 16 16"><path d="M3 1l3 3-2 2c1 2 3 4 5 5l2-2 3 3-2 3C7 15 1 9 0 3z" fill="#f47c20"/></svg>301.555.0148</li>
        <li><svg viewBox="0 0 12 12"><rect x="1" y="4" width="10" height="7" fill="#f47c20"/><rect x="3" y="1" width="6" height="3" fill="#f47c20"/></svg>(301)555-0149</li>
        <li><svg viewBox="0 0 12 12"><rect x="0" y="2" width="12" height="8" fill="#f47c20"/><path d="M0 2l6 5 6-5" stroke="#1d3f79" fill="none"/></svg>pwrobly@brantwicklaw.com</li>
        <li><svg viewBox="0 0 12 12"><rect x="0" y="2" width="12" height="8" fill="#f47c20"/><path d="M0 2l6 5 6-5" stroke="#1d3f79" fill="none"/></svg>mdunleavy@brantwicklaw.com</li>
        <li><svg viewBox="0 0 12 12"><path d="M6 12C2 7 2 5 2 4a4 4 0 018 0c0 1 0 3-4 8z" fill="#f47c20"/><circle cx="6" cy="4" r="1.5" fill="#1d3f79"/></svg><span>4820 Ridgeview Blvd, Suite 140 Rockville,<br>MD 20850</span></li>
        <li><svg viewBox="0 0 12 12"><path d="M6 12C2 7 2 5 2 4a4 4 0 018 0c0 1 0 3-4 8z" fill="#f47c20"/><circle cx="6" cy="4" r="1.5" fill="#1d3f79"/></svg><span>312 Alder Pike, Cumberland,<br>MD 21502</span></li>
        <li><svg viewBox="0 0 12 12"><path d="M6 12C2 7 2 5 2 4a4 4 0 018 0c0 1 0 3-4 8z" fill="#f47c20"/><circle cx="6" cy="4" r="1.5" fill="#1d3f79"/></svg><span>88 W Linden Street, Frederick,<br>MD 21701</span></li>
      </ul>
    </div>
    <div class="site-band">www.brantwicklaw.com</div>
  </section>

  <section class="panel panel-cover">
    <div class="cover-top">
      <div class="wordmark"><span class="mark"></span><span>Brantwick<br>Law LLC</span></div>
    </div>
    <div class="partners-photo" role="img" aria-label="Portrait of the two partners standing back to back with arms crossed"></div>
    <div class="tagline">
      <p class="ask">Ask Titans, Sharper<br>or Larger?</p>
      <p class="claim">Keen Counsel Take Verdicts.</p>
    </div>
    <div class="site-band">www.brantwicklaw.com</div>
  </section>

</main>
</body>
</html>
```